Mental Health Therapy Website

I need a design for a mental health therapy website. It is a private practice. The business name is Fenwick Counseling, PLLC. My name is Martin Fenwick, LMHC, NCC, DCC. I would like some of the features/menus to be Home; Welcome/About Me, Rates and Services, Common Questions, and Contact.
If possible I would like a blog on the main page that I can update with articles I write. I would like the contact page to feature a map to my location (4318 Harbor Pine Ave. E, Lakewood, WA 98512).
I would like to place a small photo of me on the Welcome/About page.
I am new to this so if I am forgetting anything, please ask me!!
I will upload my logo so you can fit it and the color scheme into the design.
Thank you so very much!

```html
<!DOCTYPE html>
<html lang="en">
<head>
<meta charset="utf-8">
<title>Fenwick Counseling, PLLC</title>
<link rel="stylesheet" href="https://fonts.googleapis.com/css2?family=Cinzel:wght@400;700&family=Arimo:ital,wght@0,400;0,700;1,400;1,700&display=swap">
<style>
:root{
  --green:#7aa83a;
  --green-dark:#5f8a26;
  --blue:#3a5a8e;
  --blue-dark:#2c4672;
  --navy:#1f3f74;
  --text:#3a3a3a;
  --muted:#8a8a8a;
  --footer:#2a2a2a;
  --footer-text:#8d8d8d;
  --panel:#f0f0f0;
  --line:#dcdcdc;
}
*{margin:0;padding:0;box-sizing:border-box}
html,body{width:674px;height:1200px;overflow:hidden}
body{position:relative;background:linear-gradient(#e9e9e9 50px,#fafafa 480px,#fff 520px);font-family:"Arimo",Arial,sans-serif;color:var(--text);font-size:5.6px;line-height:1.45}
.abs{position:absolute}
.site-header{position:absolute;left:0;top:0;width:674px;height:50px;background:#fff;border-bottom:2px solid var(--green)}
.brand{position:absolute;left:97px;top:9px;display:flex;align-items:center;gap:5px}
.brand-mark{width:26px;height:26px;border-radius:50%;background:var(--green)}
.brand-name{font-family:"Cinzel",serif;font-weight:700;color:var(--navy);font-size:12px;line-height:1}
.social{position:absolute;left:542px;top:9px;display:flex;gap:4px}
.social span{width:7px;height:7px;background:#a5a5a5;border-radius:1px}
.contact-line{position:absolute;right:96px;top:31px;display:flex;gap:13px;font-size:6.4px;color:#555}
.contact-line div{display:flex;align-items:center;gap:3px}
.main-nav{position:absolute;left:97px;top:71px;width:481px;height:26px;background:var(--blue);display:flex;align-items:center;font-family:"Cinzel",serif;color:#fff;font-size:10.5px}
.main-nav .item{padding:0 7px;height:26px;display:flex;align-items:center}
.main-nav .active{background:var(--green);width:59px;justify-content:center}
.main-nav .dot{width:2px;height:2px;background:#9db1d3;border-radius:50%}
.hero{position:absolute;left:105px;top:104px;width:465px;height:201px;background:linear-gradient(135deg,#dfe6ec,#c9b9a6 45%,#e7d2b8 70%,#dfe3e8);box-shadow:0 6px 8px rgba(0,0,0,.15)}
.hero .arrow{position:absolute;top:86px}
.hero-title{position:absolute;left:41px;top:127px;width:157px;height:27px;background:rgba(255,255,255,.92);font-family:"Cinzel",serif;color:var(--green);font-size:18px;line-height:27px;padding-left:5px}
.hero-sub{position:absolute;left:41px;top:156px;width:196px;height:18px;background:var(--blue);color:#fff;font-size:10px;line-height:18px;padding-left:4px}
.feature{position:absolute;top:333px;width:145px;height:168px;background:#efefef;box-shadow:0 1px 2px rgba(0,0,0,.2);text-align:center}
.feature h3{height:18px;background:var(--green);color:#fff;font-family:"Cinzel",serif;font-weight:400;font-size:8.5px;line-height:18px}
.feature .photo{margin:4px auto 0;width:139px;height:75px;background:linear-gradient(135deg,#c9b79a,#d8cdbd 50%,#9fb0c0)}
.feature .lead{margin-top:8px;color:var(--navy);font-weight:700;font-size:6.2px}
.feature p{padding:0 8px}
.btn{display:inline-block;margin-top:8px;width:49px;height:16px;line-height:16px;background:var(--blue);border:1px solid var(--blue-dark);color:#fff;font-size:5.6px}
.section-title{position:absolute;font-family:"Cinzel",serif;color:var(--navy);font-size:15.5px}
.intro{color:var(--green);font-style:italic;font-weight:700}
.about-photo{position:absolute;left:465px;top:556px;width:103px;height:60px;background:linear-gradient(90deg,#2e3238,#50545c 55%,#3a3d44)}
.blog{position:absolute;left:106px;top:652px;width:462px;height:287px;background:var(--panel);border-top:1px dotted #c8c8c8}
.post{position:absolute;left:18px;width:425px;height:64px;background:#fff;box-shadow:0 1px 2px rgba(0,0,0,.15)}
.post .thumb{position:absolute;left:10px;top:12px;width:51px;height:41px;background:linear-gradient(90deg,#2e3238,#5a5e66)}
.post .body{position:absolute;left:68px;top:10px;width:344px}
.post .more{color:var(--navy)}
.pager{position:absolute;left:385px;top:260px;display:flex;gap:3px}
.pager span{width:10px;height:10px;background:var(--blue);color:#fff;font-size:5px;text-align:center;line-height:10px;border-radius:1px}
.pager .on{background:var(--green)}
.site-footer{position:absolute;left:0;top:969px;width:674px;height:231px;background:var(--footer);color:var(--footer-text)}
.site-footer h4{position:absolute;top:35px;font-family:"Cinzel",serif;font-weight:400;color:var(--green);font-size:9.5px}
.news{position:absolute;left:107px;top:53px;width:122px}
.news .entry{padding:4px 0 5px;border-bottom:1px solid #3a3a3a}
.news b{color:#fff;font-size:6.2px}
.services{position:absolute;left:266px;top:52px;width:74px}
.services div{padding:4px 0;border-bottom:1px solid #3a3a3a}
.map{position:absolute;left:378px;top:54px;width:189px;height:91px;background:linear-gradient(135deg,#ece3cf,#e4dcc8)}
.address{position:absolute;left:378px;top:149px;color:#fff;font-weight:700;font-size:6.4px}
.bottom{position:absolute;left:97px;top:190px;width:481px;border-top:1px solid #3a3a3a;text-align:center;padding-top:13px;font-size:5.2px}
.bottom .links span{margin:0 3px}
.bottom .links .cur{color:#fff}
.to-top{position:absolute;left:647px;top:202px;width:18px;height:18px;background:#555}
</style>
</head>
<body>

<header class="site-header">
  <div class="brand"><span class="brand-mark"></span><span class="brand-name">Fenwick Counseling</span></div>
  <div class="social"><span></span><span></span><span></span></div>
  <div class="contact-line">
    <div><svg width="6" height="7" viewBox="0 0 6 7"><path d="M1 0h1.5l.5 2-1 .7a4 4 0 0 0 1.8 2l.7-.9 1.5.6V6l-1 1C2 6.5 0 4 0 1z" fill="#7aa83a"/></svg>000000000000</div>
    <div><svg width="8" height="6" viewBox="0 0 8 6"><rect width="8" height="6" fill="#7aa83a"/><path d="M0 0l4 3 4-3" stroke="#fff" stroke-width=".7" fill="none"/></svg>info@companyname.com</div>
  </div>
</header>

<nav class="main-nav">
  <span class="item active">Home</span>
  <span class="item">About Me</span><span class="dot"></span>
  <span class="item">Rates and Services</span><span class="dot"></span>
  <span class="item">Common Questions</span><span class="dot"></span>
  <span class="item">Contact</span>
</nav>

<section class="hero" role="img" aria-label="Slide photo: smiling family of four with their dog">
  <svg class="arrow" style="left:8px" width="10" height="26" viewBox="0 0 10 26"><path d="M9 1L1 13l8 12" stroke="#333" stroke-width="1.2" fill="none"/></svg>
  <svg class="arrow" style="right:8px" width="10" height="26" viewBox="0 0 10 26"><path d="M1 1l8 12-8 12" stroke="#333" stroke-width="1.2" fill="none"/></svg>
  <div class="hero-title">Lorem Ipsum</div>
  <div class="hero-sub">Nulla lobortis consequat mauris, eget</div>
</section>

<article class="feature" style="left:106px">
  <h3>Lorem ipsum dolor</h3>
  <div class="photo" role="img" aria-label="Photo: family counseling session on a sofa"></div>
  <div class="lead">Lorem ipsum dolor sit amet, consectetur</div>
  <p>adipiscing elit. Nulla lobortis consequat mauris, eget eleifend nunc viverra viverra. Ut ac risus odio. Aliquam pretium purus sed nulla</p>
  <span class="btn">Read More</span>
</article>
<article class="feature" style="left:265px">
  <h3>Lorem ipsum dolor</h3>
  <div class="photo" role="img" aria-label="Photo: therapist taking notes" style="background:linear-gradient(90deg,#d9c6b2,#eef0f2)"></div>
  <div class="lead">Lorem ipsum dolor sit amet, consectetur</div>
  <p>adipiscing elit. Nulla lobortis consequat mauris, eget eleifend nunc viverra viverra. Ut ac risus odio. Aliquam pretium purus sed nulla</p>
  <span class="btn">Read More</span>
</article>
<article class="feature" style="left:424px">
  <h3>Lorem ipsum dolor</h3>
  <div class="photo" role="img" aria-label="Photo: older man talking with a counselor" style="background:linear-gradient(90deg,#8fa9c6,#c9c2b8 60%,#e6e6e6)"></div>
  <div class="lead">Lorem ipsum dolor sit amet, consectetur</div>
  <p>adipiscing elit. Nulla lobortis consequat mauris, eget eleifend nunc viverra viverra. Ut ac risus odio. Aliquam pretium purus sed nulla</p>
  <span class="btn">Read More</span>
</article>

<h2 class="section-title" style="left:107px;top:529px">About Me</h2>
<div class="abs" style="left:107px;top:553px;width:350px">
  <p class="intro">Lorem ipsum dolor sit amet, consectetur adipiscing elit. Nulla lobortis consequat mauris, eget eleifend nunc viverra viverra. Ut ac risus odio. Aliquam pretium purus sed nulla feugiat blandit. Cras vel libero ut lacus eleifend tempor.</p>
  <p style="margin-top:7px">Lorem ipsum dolor sit amet, consectetur adipiscing elit. Nulla lobortis consequat mauris, eget eleifend nunc viverra viverra. Ut ac risus odio. Aliquam pretium purus sed nulla feugiat blandit. Cras vel libero ut lacus eleifend tempor. Phasellus eleifend, magna non tincidunt accumsan, justo arcu cursus ipsum, non porttitor sapien quam vel magna. Maecenas elit nisl, molestie nec dapibus nec, aliquet a erat. Donec scelerisque lacus a libero suscipit auctor volutpat enim euismod. Mauris porta, lacus ut ullamcorper sodales, mauris tortor feugiat purus Mauris porta, lacus ut ullamcorper sodales, mauris tortor feugiat purus.</p>
</div>
<div class="about-photo" role="img" aria-label="Portrait photo of Martin Fenwick"></div>

<section class="blog">
  <h2 class="section-title" style="left:17px;top:12px">Blog</h2>
  <article class="post" style="top:38px">
    <div class="thumb" role="img" aria-label="Author portrait"></div>
    <div class="body"><p class="intro">Lorem ipsum dolor sit amet, consectetur adipiscing elit. Nulla lobortis consequat mauris, eget eleifend nunc viverra viverra.</p>
    <p style="margin-top:4px">Lorem ipsum dolor sit amet, consectetur adipiscing elit. Nulla lobortis consequat mauris, eget eleifend nunc viverra viverra. Ut ac risus odio. Aliquam pretium purus sed nulla feugiat blandit. Cras vel libero ut lacus eleifend tempor. Phasellus eleifend, magna non tincidunt accumsan, justo arcu cursus ipsum, non porttitor sapien quam vel magna. Maecenas elit nisl, molestie nec dapibus nec,</p>
    <span class="more">read more...</span></div>
  </article>
  <article class="post" style="top:110px">
    <div class="thumb" role="img" aria-label="Author portrait"></div>
    <div class="body"><p class="intro">Lorem ipsum dolor sit amet, consectetur adipiscing elit. Nulla lobortis consequat mauris, eget eleifend nunc viverra viverra.</p>
    <p style="margin-top:4px">Lorem ipsum dolor sit amet, consectetur adipiscing elit. Nulla lobortis consequat mauris, eget eleifend nunc viverra viverra. Ut ac risus odio. Aliquam pretium purus sed nulla feugiat blandit. Cras vel libero ut lacus eleifend tempor. Phasellus eleifend, magna non tincidunt accumsan, justo arcu cursus ipsum, non porttitor sapien quam vel magna. Maecenas elit nisl, molestie nec dapibus nec,</p>
    <span class="more">read more...</span></div>
  </article>
  <article class="post" style="top:183px">
    <div class="thumb" role="img" aria-label="Author portrait"></div>
    <div class="body"><p class="intro">Lorem ipsum dolor sit amet, consectetur adipiscing elit. Nulla lobortis consequat mauris, eget eleifend nunc viverra viverra.</p>
    <p style="margin-top:4px">Lorem ipsum dolor sit amet, consectetur adipiscing elit. Nulla lobortis consequat mauris, eget eleifend nunc viverra viverra. Ut ac risus odio. Aliquam pretium purus sed nulla feugiat blandit. Cras vel libero ut lacus eleifend tempor. Phasellus eleifend, magna non tincidunt accumsan, justo arcu cursus ipsum, non porttitor sapien quam vel magna. Maecenas elit nisl, molestie nec dapibus nec,</p>
    <span class="more">read more...</span></div>
  </article>
  <div class="pager"><span class="on">1</span><span>2</span><span>3</span><span>4</span><span>5</span></div>
</section>

<footer class="site-footer">
  <h4 style="left:107px">Latest News</h4>
  <h4 style="left:266px">Services</h4>
  <h4 style="left:377px">Contact Us</h4>
  <div class="news">
    <div class="entry"><b>21.02.2014</b><br>Adipiscing elit. Nulla lobortis consequat mauris, eget eleifend nunc viverra viverra. Ut ac risus odio. Aliquam pretium purus sed nulla</div>
    <div class="entry"><b>22.02.2014</b><br>Nulla lobortis consequat mauris, eget eleifend nunc viverra viverra. Ut ac risus odio.</div>
    <div class="entry" style="border:0"><b>23.02.2014</b><br>Lobortis consequat mauris, eget eleifend nunc viverra viverra. Ut ac risus odio. Aliquam pretium purus sed nulla feugiat blandit.</div>
  </div>
  <div class="services">
    <div>Lorem ipsum dolor sit amet,</div>
    <div>Consectetur adipiscing elit.</div>
    <div>Nulla lobortis consequat</div>
    <div>Mauris, eget eleifend nunc</div>
    <div>Viverra viverra. Ut ac risus</div>
    <div>Odio. Aliquam pretium purus</div>
    <div style="border:0">Sed nulla feugiat blandit.</div>
  </div>
  <div class="map" role="img" aria-label="Street map showing the office location">
    <svg class="abs" style="left:93px;top:34px" width="8" height="11" viewBox="0 0 8 11"><path d="M4 11C1 6 0 5 0 4a4 4 0 0 1 8 0c0 1-1 2-4 7z" fill="#d42a2a"/><circle cx="4" cy="4" r="1.4" fill="#fff"/></svg>
  </div>
  <div class="address">4318 Harbor Pine Ave. E, Lakewood, WA 98512</div>
  <div class="bottom">
    <div class="links"><span class="cur">Home</span>•<span>About Me</span>•<span>Rates and Services</span>•<span>Common Questions</span>•<span>Contact</span></div>
    <div>© Copyright 2014 Fenwick Counseling, PLLC. All Rights Reserved.</div>
  </div>
  <div class="to-top"><svg width="18" height="18" viewBox="0 0 18 18"><path d="M5 11l4-4 4 4" stroke="#ddd" stroke-width="1" fill="none"/></svg></div>
</footer>

</body>
</html>
```